Flyer for teen fitness class at a physiotherapy clinic

We are a passionate Physiotherapy Clinic requiring a flyer to promote our new service a fitness class for teenagers, which is called Youth's FLX - Flexible Limber Xtra Power. The aim of the class is to prevents injuries in sports, improve sporting performance and provide safe activity for otherwise inactive teens. The aim of the flyer is to make people aware of this new service and interested in joining. Ideally the Flyer would incorporate blue colours. Our logo must be on the flier, and at least one or two of the photos provided. Our logo is provided in the attachments. Required information : Youth's FLX: Flexible Limber Xtra Power, times Mondays and Wednesdays 4 -5. Can be claimed on private health insurance. Expert advice to tailor a program to individual needs. For more information go www.rmpvq.com.au or phone 03)5871 6093.

Industry/Entity Type

Clinic

```html
<!DOCTYPE html>
<html lang="en">
<head>
<meta charset="utf-8">
<title>Youth's FLX - Flexible Limber Xtra Power</title>
<link href="https://fonts.googleapis.com/css2?family=Bebas+Neue&display=swap" rel="stylesheet">
<style>
  :root {
    --ink: #0b0b0b;
    --brand-blue: #0d3f94;
    --mid-blue: #1e56b0;
    --sky-blue: #4aa3e8;
    --pale-blue: #c9ddf0;
    --teal: #2a9a87;
    --white: #ffffff;
    --bg-top: #f4f7fb;
    --bg-bottom: #e6eef7;
    --shirt-blue: #4a5fb8;
    --shirt-grey: #cfd2d6;
    --skin: #d9a48c;
  }
  html, body {
    margin: 0;
    padding: 0;
    overflow: hidden;
  }
  .flyer {
    position: relative;
    width: 1200px;
    height: 850px;
    overflow: hidden;
    background: linear-gradient(180deg, var(--bg-top) 0%, var(--white) 40%, var(--bg-bottom) 100%);
    font-family: "Bebas Neue", "Oswald", sans-serif;
  }
  .bands, .splash {
    position: absolute;
    left: 0;
    top: 0;
    width: 1200px;
    height: 850px;
  }
  .teen-photo {
    position: absolute;
    border-radius: 60px 60px 0 0;
  }
  .teen-photo--left {
    left: 60px;
    top: 300px;
    width: 370px;
    height: 550px;
    background: linear-gradient(180deg, var(--skin) 0%, var(--skin) 55%, var(--shirt-blue) 70%, var(--shirt-blue) 100%);
  }
  .teen-photo--right {
    left: 565px;
    top: 342px;
    width: 300px;
    height: 508px;
    background: linear-gradient(180deg, var(--skin) 0%, var(--skin) 60%, var(--shirt-grey) 72%, var(--shirt-grey) 100%);
  }
  .headline {
    position: absolute;
    left: 42px;
    top: 34px;
    margin: 0;
    font-weight: 400;
    line-height: 1;
    white-space: nowrap;
  }
  .headline__lead {
    font-size: 172px;
    color: var(--ink);
    letter-spacing: 1px;
  }
  .headline__name {
    font-size: 224px;
    color: var(--brand-blue);
    letter-spacing: 2px;
    margin-left: 6px;
    text-shadow: 2px 3px 4px rgba(0,0,0,0.18);
  }
  .subtitle {
    position: absolute;
    left: 46px;
    top: 212px;
    margin: 0;
    font-weight: 400;
    font-size: 76px;
    line-height: 1;
    color: var(--ink);
    letter-spacing: 1px;
    white-space: nowrap;
  }
  .clinic-mark {
    position: absolute;
    left: 812px;
    top: 128px;
    display: flex;
    align-items: center;
    gap: 14px;
  }
  .clinic-mark__dot {
    width: 22px;
    height: 22px;
    border-radius: 50%;
    background: var(--sky-blue);
    flex: none;
  }
  .clinic-mark__name {
    font-size: 44px;
    line-height: 0.95;
    color: var(--brand-blue);
  }
  .schedule {
    position: absolute;
    left: 868px;
    top: 432px;
    width: 316px;
    height: 380px;
  }
  .schedule svg {
    position: absolute;
    left: 0;
    top: 0;
  }
  .schedule__text {
    position: absolute;
    left: 30px;
    top: 66px;
    width: 280px;
    margin: 0;
    text-align: center;
    color: var(--white);
    line-height: 1;
  }
  .schedule__days {
    font-size: 54px;
    display: block;
    line-height: 0.95;
  }
  .schedule__time {
    font-size: 120px;
    display: block;
    margin-top: 6px;
  }
</style>
</head>
<body>
<main class="flyer">
  <svg class="bands" viewBox="0 0 1200 850" aria-hidden="true">
    <polygon points="0,445 640,392 640,402 0,470" fill="var(--pale-blue)"/>
    <polygon points="0,500 1200,282 1200,332 0,612" fill="var(--brand-blue)"/>
    <polygon points="640,440 1200,300 1200,318 700,436" fill="var(--sky-blue)"/>
    <polygon points="760,430 1200,330 1200,368 800,432" fill="var(--sky-blue)"/>
  </svg>

  <svg class="splash" viewBox="0 0 1200 850" role="img" aria-label="Splashing wave background">
    <defs>
      <linearGradient id="splash" x1="0" y1="0" x2="0" y2="1">
        <stop offset="0" stop-color="#dcebf7"/>
        <stop offset="0.5" stop-color="#a9cfee"/>
        <stop offset="1" stop-color="#7fb6e2"/>
      </linearGradient>
    </defs>
    <polygon points="0,612 1200,368 1200,850 0,850" fill="url(#splash)"/>
  </svg>

  <div class="teen-photo teen-photo--left" role="img" aria-label="Photo of a smiling teenage girl in a blue t-shirt jumping with arms raised"></div>
  <div class="teen-photo teen-photo--right" role="img" aria-label="Photo of a smiling teenage boy in a cap and grey singlet jumping with arms raised"></div>

  <h1 class="headline">
    <span class="headline__lead">YOUTH'S</span><span class="headline__name">FLX</span>
  </h1>
  <p class="subtitle">FLEXIBLE LIMBER XTRA POWER</p>

  <div class="clinic-mark">
    <span class="clinic-mark__dot"></span>
    <span class="clinic-mark__name">Harbourline<br>Sports Treatment Clinic</span>
  </div>

  <div class="schedule">
    <svg width="316" height="380" viewBox="0 0 316 380" aria-hidden="true">
      <ellipse cx="150" cy="192" rx="146" ry="184" fill="var(--brand-blue)"/>
      <ellipse cx="158" cy="190" rx="146" ry="184" fill="var(--mid-blue)"/>
      <ellipse cx="168" cy="188" rx="144" ry="182" fill="var(--teal)"/>
    </svg>
    <p class="schedule__text">
      <span class="schedule__days">MONDAYS<br>AND<br>WEDNESDAYS</span>
      <span class="schedule__time">4 -5</span>
    </p>
  </div>
</main>
</body>
</html>
```